Brightpath Tech Academy by graduating students from college in two years

Based on the logo design, create stationary and business cards for
Dr. Velimir T Osunde, CEO, (703) 482-1630
and Mirela Thorpe, Respresentative, (301) 557-2048
Address: 4417 Marbleton Lane, Faurfax Station, VA 22061
Incorporate elelments of the logo

Target Market(s)

USA

Other font styles liked:
• match with the logo type style

```html
<!DOCTYPE html>
<html lang="en">
<head>
<meta charset="utf-8">
<title>Brightpath Tech Academy Letterhead</title>
<link rel="stylesheet" href="https://fonts.googleapis.com/css2?family=Arimo:wght@400;700&display=swap">
<style>
  :root {
    --navy: #1d2758;
    --gold: #fbc531;
    --paper: #ffffff;
    --backdrop: #e4e4e4;
    --ink: #222222;
    --rule: #5a6690;
  }
  * { margin: 0; padding: 0; box-sizing: border-box; }
  html, body {
    width: 1200px;
    height: 1200px;
    overflow: hidden;
    background: var(--backdrop);
    font-family: "Arimo", Arial, sans-serif;
  }
  .letterhead {
    position: absolute;
    left: 200px;
    top: 34px;
    width: 800px;
    height: 1132px;
    background: var(--paper);
    overflow: hidden;
  }
  .band {
    position: absolute;
  }
  .band--navy { background: var(--navy); }
  .band--gold { background: var(--gold); }
  .band--top-gold    { left: 0;     top: 0;      width: 800px; height: 12px; }
  .band--top-navy    { right: 0;    top: 12px;   width: 360px; height: 10px; }
  .band--bottom-navy { left: 0;     bottom: 12px; width: 800px; height: 6px; }
  .band--bottom-gold { left: 0;     bottom: 0;   width: 800px; height: 12px; }

  .brand {
    position: absolute;
    left: 58px;
    top: 90px;
    display: flex;
    align-items: center;
    gap: 12px;
    color: var(--navy);
    font-weight: 700;
    font-size: 19px;
    line-height: 1.2;
  }
  .brand__dot {
    width: 46px;
    height: 46px;
    border-radius: 50%;
    background: var(--gold);
    flex: none;
  }
  .contacts {
    position: absolute;
    right: 43px;
    top: 84px;
    text-align: right;
    color: var(--ink);
    font-size: 16px;
    line-height: 20px;
  }
  .contact + .contact { margin-top: 18px; }
  .header-rule {
    position: absolute;
    left: 47px;
    right: 43px;
    top: 205px;
    height: 2px;
    background: var(--rule);
  }
  .address {
    position: absolute;
    left: 0;
    right: 0;
    top: 1072px;
    text-align: center;
    color: var(--ink);
    font-size: 16px;
  }
</style>
</head>
<body>
  <main class="letterhead">
    <div class="band band--gold band--top-gold"></div>
    <div class="band band--navy band--top-navy"></div>

    <div class="brand">
      <span class="brand__dot"></span>
      <span class="brand__name">Brightpath<br>Tech Academy</span>
    </div>

    <div class="contacts">
      <p class="contact">Dr. Velimir T Osunde, CEO<br>(703) 482-1630</p>
      <p class="contact">Mirela Thorpe, Respresentative<br>(301) 557-2048</p>
    </div>

    <div class="header-rule"></div>

    <p class="address">4417 Marbleton Lane, Faurfax Station, VA 22061</p>

    <div class="band band--navy band--bottom-navy"></div>
    <div class="band band--gold band--bottom-gold"></div>
  </main>
</body>
</html>
```